Poster is for a beauty clinic to advertise the cosmetic injection section which performs Lumiq and Dermal Fillers treatments. The treatments are undertaken by Dr Sunil Varma a highly acclaimed Wexmoor Street Practioner . The following words must be mentioned though you can add more words if you want: Cosmetic Injection Clinic @ Velvora Beauty
Lumiq, Dermal Fillers, Stay Younger, Rejuvenate, Dr Sunil Varma Highly Acclaimed Wexmoor Street, Book at Reception, www.glowmendclinics.co.uk
Poster must be a stand out very classy and exclusive poster
SIZE OF POSTER A1

```html
<!DOCTYPE html>
<html lang="en">
<head>
<meta charset="utf-8">
<title>Cosmetic Injection Clinic @ Velvora Beauty</title>
<link rel="stylesheet" href="https://fonts.googleapis.com/css2?family=Roboto+Condensed:wght@300;400;700&family=Oswald:wght@600;700&display=swap">
<style>
  :root {
    --orange: #f39a1e;
    --orange-deep: #e8830c;
    --orange-soft: #f7b55a;
    --charcoal: #2b2b2b;
    --white: #ffffff;
    --skin-light: #f1d2bd;
    --skin-mid: #d9a98c;
    --hair: #5a3e2e;
  }
  html, body { margin: 0; padding: 0; overflow: hidden; }
  body { width: 849px; height: 1200px; background: var(--white); }
  .poster {
    position: relative; width: 849px; height: 1200px; overflow: hidden;
    background: var(--white);
    font-family: "Roboto Condensed", Arial, sans-serif;
    color: var(--white);
  }
  .model-photo { position: absolute; left: 0; top: 60px; width: 760px; height: 1140px; }
  .poster-shapes { position: absolute; inset: 0; }
  .clinic-title {
    position: absolute; right: 26px; top: 14px; margin: 0;
    text-align: right; font-weight: 300; font-size: 54px; line-height: 0.95;
    letter-spacing: 0.5px; text-transform: uppercase;
  }
  .treatments {
    position: absolute; left: 522px; top: 598px; width: 310px;
  }
  .treatments-heading { margin: 0 0 6px; font-weight: 300; font-size: 30px; white-space: nowrap; }
  .treatment-list { list-style: none; margin: 0; padding: 0; }
  .treatment-list li {
    position: relative; padding-left: 26px; font-size: 38px; font-weight: 400; line-height: 1.05;
    white-space: nowrap;
  }
  .treatment-list li::before {
    content: ""; position: absolute; left: 4px; top: 16px;
    width: 12px; height: 12px; border-radius: 50%; background: var(--white);
  }
  .tagline {
    position: absolute; left: 455px; top: 738px; width: 394px; height: 118px; margin: 0;
    background: var(--charcoal); box-sizing: border-box; padding: 10px 0 0 18px;
    font-family: "Oswald", Impact, sans-serif; font-weight: 700; line-height: 1;
    text-transform: uppercase;
  }
  .tagline-main { display: block; color: var(--orange); font-size: 52px; }
  .tagline-sub { display: block; color: var(--white); font-size: 46px; margin-top: 4px; }
  .practitioner {
    position: absolute; left: 22px; bottom: 26px; margin: 0;
    font-weight: 300; font-size: 27px; line-height: 1.08;
  }
  .practitioner .web { font-size: 21px; }
</style>
</head>
<body>
<main class="poster">
  <svg class="model-photo" viewBox="0 0 760 1140" role="img" aria-label="Photograph of a woman with eyes closed, hands framing her face, smooth glowing skin">
    <defs>
      <radialGradient id="skinTone" cx="50%" cy="38%" r="55%">
        <stop offset="0%" stop-color="var(--skin-light)"/>
        <stop offset="60%" stop-color="var(--skin-mid)" stop-opacity="0.85"/>
        <stop offset="100%" stop-color="var(--skin-mid)" stop-opacity="0"/>
      </radialGradient>
    </defs>
    <ellipse cx="330" cy="560" rx="390" ry="600" fill="url(#skinTone)"/>
  </svg>

  <svg class="poster-shapes" width="849" height="1200" viewBox="0 0 849 1200" aria-hidden="true">
    <path d="M150 0 H849 V360 C720 345 600 310 470 240 C330 165 230 90 150 0 Z" fill="var(--orange-soft)"/>
    <path d="M230 0 H849 V335 C730 320 610 285 500 225 C380 160 290 85 230 0 Z" fill="var(--orange)"/>
    <rect class="treatments-panel" x="500" y="586" width="349" height="152" fill="var(--orange)"/>
    <path d="M0 930 C180 990 420 1000 849 930 V1200 H0 Z" fill="var(--orange-soft)"/>
    <path d="M0 980 C220 1040 480 1030 849 960 V1200 H0 Z" fill="var(--orange)"/>
    <path d="M0 1150 C300 1100 600 1130 849 1090 V1200 H0 Z" fill="var(--orange-deep)"/>
  </svg>

  <h1 class="clinic-title">Cosmetic<br>Injection<br>Clinic<br>@Velvora<br>Beauty</h1>

  <section class="treatments">
    <p class="treatments-heading">Treatments we perform</p>
    <ul class="treatment-list">
      <li>Lumiq</li>
      <li>Dermal Fillers</li>
    </ul>
  </section>

  <p class="tagline">
    <span class="tagline-main">Stay Younger</span>
    <span class="tagline-sub">Rejuvenate</span>
  </p>

  <p class="practitioner">
    All the treatments are undertaken by Dr Sunil Varma<br>
    A highly acclaimed Wexmoor Street Practioner.<br>
    Book at Reception.<br>
    <span class="web">to get more details visit our web site: www.glowmendclinics.co.uk</span>
  </p>
</main>
</body>
</html>
```